Broschüre für Premium Marke
Der Designer hat definitiv eine gute Auffassungsgabe und ein Gefühl dafür, was der Kunde will. Auf jeden Fall zu empfehlen. 1:1 - Projekte folgen bestimmt! MfG

```html
<!DOCTYPE html>
<html lang="de">
<head>
<meta charset="utf-8">
<title>Velunio – Broschüre</title>
<link href="https://fonts.googleapis.com/css2?family=Roboto+Slab:wght@400;700&family=Open+Sans:wght@400;600;700&display=swap" rel="stylesheet">
<style>
:root{
  --stage:#d9d9d9;
  --paper:#f7f7f7;
  --paper-warm:#efefef;
  --ink:#0a0a0c;
  --charcoal:#2a2a2b;
  --white:#ffffff;
  --grey-text:#c9c9c9;
  --body-text:#4a4a4a;
  --crimson:#a8183f;
  --steel:#4a86b0;
  --sage:#5f9e83;
  --plum:#a0246f;
  --mint:#6fb59a;
}
*{box-sizing:border-box;margin:0;padding:0}
html,body{width:1200px;height:848px;overflow:hidden;background:var(--stage)}
body{position:relative;font-family:"Open Sans",sans-serif}
.page{position:absolute;background:var(--paper);overflow:hidden}
.brand{position:absolute;left:0;right:0;display:flex;align-items:center;justify-content:center;gap:4px;font-family:"Open Sans",sans-serif;font-weight:600;letter-spacing:.2px}
.brand .mark{display:inline-block;background:currentColor}

/* spread */
.spread-left{left:40px;top:155px;width:380px;height:537px;box-shadow:inset -18px 0 22px -14px rgba(0,0,0,.25)}
.spread-right{left:420px;top:155px;width:380px;height:537px;box-shadow:inset 18px 0 22px -14px rgba(0,0,0,.18)}
.overview-panel{position:absolute;left:0;top:12px;width:338px;height:448px;background:var(--ink);border-radius:0 26px 26px 0}
.overview-title{position:absolute;left:78px;top:24px;font-family:"Roboto Slab",serif;font-weight:700;font-size:14px;color:var(--white);letter-spacing:.4px}
.line-row{position:absolute;left:0;width:338px;height:100px}
.line-photo{position:absolute;left:0;top:0;width:54px;height:100px}
.line-tag{position:absolute;left:18px;bottom:12px;padding:3px 9px;font-family:"Roboto Slab",serif;font-size:13px;color:var(--white);border-radius:0 6px 6px 0;letter-spacing:.5px}
.line-desc{position:absolute;left:78px;width:220px;font-size:7.5px;line-height:1.45;color:var(--grey-text)}
.line-desc b{color:var(--white);font-weight:700}
.tag-steelix{background:var(--crimson)}
.tag-vista{background:var(--steel)}
.tag-sprinto{background:var(--sage)}
.tag-crista{background:var(--plum)}

.detail-frame{position:absolute;left:10px;top:16px;width:346px;height:452px;border:1.2px solid var(--mint);border-radius:0 26px 26px 0}
.detail-photo{position:absolute;left:22px;top:30px;width:132px;height:196px;border-radius:0 20px 20px 20px}
.detail-tag{position:absolute;left:66px;top:208px;padding:4px 10px;background:var(--sage);font-family:"Roboto Slab",serif;font-size:15px;color:var(--white);border-radius:0 7px 7px 0;letter-spacing:.6px}
.detail-kicker{position:absolute;left:22px;top:248px;font-family:"Roboto Slab",serif;font-size:7.5px;color:var(--sage)}
.detail-copy{position:absolute;left:22px;top:262px;width:128px;font-size:6.3px;line-height:1.55;color:var(--body-text)}
.range-head{position:absolute;left:176px;font-family:"Roboto Slab",serif;font-size:7px;color:var(--sage);letter-spacing:.4px}
.range-block{position:absolute;left:176px;width:150px;border-radius:4px}
.feature{position:absolute;left:176px;display:flex;align-items:center;gap:6px;font-size:5.5px;color:#777;letter-spacing:.6px}
.feature svg{width:16px;height:16px}
.next-edge{position:absolute;right:0;top:26px;width:8px;height:440px;border-left:1.2px solid var(--plum);border-top:1.2px solid var(--plum);border-radius:8px 0 0 0}

/* covers */
.cover{left:880px;width:270px;height:382px;box-shadow:0 6px 14px rgba(0,0,0,.12)}
.cover-front{top:22px}
.cover-back{top:444px}
.cover-panel{position:absolute;left:8px;top:8px;width:254px;height:336px;border-radius:0 24px 0 24px}
.cover-front .cover-panel{background:var(--charcoal)}
.cover-back .cover-panel{background:var(--ink)}
.imprint{position:absolute;left:0;right:0;top:276px;text-align:center;font-size:4.6px;line-height:1.5;color:#8d8d8d}
.imprint b{color:#bdbdbd}
</style>
</head>
<body>

<!-- spread: overview page -->
<section class="page spread-left" aria-label="Sortimentsübersicht">
  <div class="overview-panel">
    <h2 class="overview-title">SORTIMENTSÜBERSICHT</h2>

    <div class="line-row" style="top:50px">
      <div class="line-photo" role="img" aria-label="Foto: Edelstahlflasche im Auto" style="background:linear-gradient(160deg,#3b4a52,#7f8a7c)"></div>
      <p class="line-desc" style="top:10px"><b>Der Klassiker</b> – aus hochwertigem 18/8 Edelstahl als Trinkflasche und Vakuum-Isolierflasche</p>
      <span class="line-tag tag-steelix">STEELIX</span>
    </div>

    <div class="line-row" style="top:152px">
      <div class="line-photo" role="img" aria-label="Foto: Frau mit Mütze trinkt im Freien" style="background:linear-gradient(160deg,#9aa3a6,#5e4b3f)"></div>
      <p class="line-desc" style="top:24px"><b>Der Eye-Catcher</b> – aus Kelvar von Corvane USA als Trinkflasche und doppelwandige Isolierflasche</p>
      <span class="line-tag tag-vista">VISTA</span>
    </div>

    <div class="line-row" style="top:254px">
      <div class="line-photo" role="img" aria-label="Foto: Läuferin im Park" style="background:linear-gradient(160deg,#6f8f4e,#8a8f96)"></div>
      <p class="line-desc" style="top:30px"><b>Für Sportler</b> am Limit – zum Squeezen, als Trinkflasche und doppelwandige Isolierflasche</p>
      <span class="line-tag tag-sprinto">SPRINTO</span>
    </div>

    <div class="line-row" style="top:348px">
      <div class="line-photo" role="img" aria-label="Foto: Wanderer in Herbstlandschaft" style="background:linear-gradient(160deg,#4a5d7a,#8a7a3c)"></div>
      <p class="line-desc" style="top:28px"><b>Die Zeitlose</b> – aus hitzebeständigem Borosilikat-Glas als Trinkflasche mit transparent farbiger Silikonhülle</p>
      <span class="line-tag tag-crista">CRISTA</span>
    </div>
  </div>
  <div class="brand" style="top:486px;font-size:11px;color:var(--ink)"><span class="mark" style="width:8px;height:8px"></span>velunio</div>
</section>

<!-- spread: product line page -->
<section class="page spread-right" aria-label="Produktlinie Sprinto">
  <div class="detail-frame"></div>
  <div class="detail-photo" role="img" aria-label="Foto: Läuferin trinkt aus der Sportflasche im Park" style="background:linear-gradient(170deg,#5f8a44 0%,#8fae6a 45%,#7aa0c2 70%,#8b8e94 100%)"></div>
  <span class="detail-tag">SPRINTO</span>
  <h3 class="detail-kicker">Die Sportflasche</h3>
  <p class="detail-copy">Die Ziellinie ist erreicht oder noch in weiter Ferne. Die Sonne brennt dir direkt ins Gesicht und du hältst am Lenkrad deines Fahrrads – kein Problem, denn deine Flasche steckt am Gurt oder in der Halterung und du genießt das kalte, klare Wasser. Mit dieser High-Tech-Trinkflasche bist du immer bereit zum Aufbruch, immer bereit, dich selbst zu übertreffen, und das Beste aus dir herauszuholen. Squeeze die Flasche und stille in Sekunden deinen Durst, ohne beim Marathon Zeit zu verlieren. Auf dem Rad unterwegs brauchst du nicht anzuhalten – nimm deine Flasche mit einer Hand und trinke mit dem innovativen Push-Pull-Verschluss. Die Halterung ist einfach zu befestigen, die Flasche passt in jeden Geschirrspüler. So stellst du dich mit Freude jeden Tag neuen Herausforderungen!</p>

  <h4 class="range-head" style="top:40px">LOREM IPSUM</h4>
  <div class="range-block" role="img" aria-label="Produktfotos: Sportflaschen in Grau, Schwarz und Rot" style="top:54px;height:110px;background:linear-gradient(90deg,#b9bcc0,#5a5d63 40%,#9a3a44 75%,#c7c9cc)"></div>
  <h4 class="range-head" style="top:176px">LOREM IPSUM</h4>
  <div class="range-block" role="img" aria-label="Produktfotos: Sportflaschen in Gelb, Blau und Rot" style="top:190px;height:120px;background:linear-gradient(90deg,#c9c23a,#3a67b2 40%,#c43338 75%,#3b6fb5)"></div>

  <div class="feature" style="top:420px">
    <svg viewBox="0 0 16 16" aria-hidden="true"><circle cx="8" cy="8" r="7" fill="none" stroke="#888" stroke-width="1"/><path d="M5 11 L11 5 M8 4.5 C6.5 7 6 8 6 9 A2 2 0 0 0 10 9 C10 8 9.5 7 8 4.5Z" fill="none" stroke="#888" stroke-width=".8"/></svg>
    LEAK-PROOF
  </div>
  <div class="feature" style="top:442px">
    <svg viewBox="0 0 16 16" aria-hidden="true"><circle cx="8" cy="8" r="7" fill="none" stroke="#888" stroke-width="1"/><path d="M4 12 L12 4" stroke="#888" stroke-width=".8"/><rect x="5" y="6" width="6" height="4" fill="none" stroke="#888" stroke-width=".8"/></svg>
    BPA FREE
  </div>
  <div class="next-edge"></div>
  <div class="brand" style="top:488px;font-size:11px;color:var(--ink)"><span class="mark" style="width:8px;height:8px"></span>velunio</div>
</section>

<!-- front cover -->
<section class="page cover cover-front" aria-label="Titelseite">
  <div class="cover-panel"></div>
  <div class="brand" style="top:258px;font-size:24px;color:#141414"><span class="mark" style="width:16px;height:16px"></span>velunio</div>
</section>

<!-- back cover -->
<section class="page cover cover-back" aria-label="Rückseite">
  <div class="cover-panel"></div>
  <address class="imprint" style="font-style:normal">
    <b>VELUNIO EUROPE GmbH</b><br>
    Musterweg 12<br>
    20000 Hansestadt<br><br>
    T +49 40 0000 0000<br>
    F +49 40 0000 0001<br>
    info@velunio-beispiel.de<br>
    www.velunio-beispiel.de
  </address>
  <div class="brand" style="top:356px;font-size:10px;color:var(--ink)"><span class="mark" style="width:7px;height:7px"></span>velunio</div>
</section>

</body>
</html>
```